Modern book cover design

We are looking for a modern, powerful book cover for a general intrest book about how robots are going to take human jobs in the future.

The book title is "Torvanique"

It also has a strap line "The close of human work and how automatons will supplant it"
Both the title and the strap line should be on the front cover

I have attached a number of book designs I like, and my author picture.

Reason: Some great submissions but none quite have that wow factor

Target Market(s)

This is a general intrest book, but the reader is likely to be male 30-50

Requirements
Must have
• -Title "Torvanique"

-Strap-line "The close of human work and how automatons will supplant it"

-Be compliant with PrintMoraly Cover Design Criteria(www.printmoraly.example)

-Book size : 5.5 x 8.5 inches

-Spine size : 0.625 inches

-Must have one author picture on the back cover(attached)

-Must have the following author description on back cover:
"Tom Hollis is a leading futurologist, technologist, inventor, and entrepreneur. With over twenty years of experience in technology and innovation, Tom has travelled the world seeking out and developing new technologies. As a leading voice on the challenges and benefits of tomorrow’s technology, he has advised some of the world’s leading institutions, including the Grand Chancery, regarding technological preparations for the future. He is the recipient of the centennial founder of the season prize and has appeared on numerous technology and philanthropy television programs, as well as presenting Clever Little Marvels on Robotics."

-Must have the following book description on back cover:
“Torvanique is a look at the rapidly changing face of robotics and how it will revolutionize employment over the next thirty years. Tom Hollis lays out the arguments in favor of and against the mechanization of our society, as well as the advantages and untold risks as we march into this ever-present future.”

-Must have the following quote on the back cover:
"A fascinating look into the future of robotics and their impact on humanity, be prepared to question when robots will replace you - Derek Pallister, Professor of Cybernetics at the University of Castlemere”

-Example barcode

```html
<!DOCTYPE html>
<html lang="en">
<head>
<meta charset="utf-8">
<title>Torvanique – Tom Hollis</title>
<link rel="stylesheet" href="https://fonts.googleapis.com/css2?family=Michroma&family=Dosis:wght@200;300&display=swap">
<style>
  :root {
    --backdrop: #3b4349;
    --cover-glow: #e41f26;
    --cover-mid: #b8191f;
    --cover-edge: #97151a;
    --ink-light: #ffffff;
    --ink-soft: #f4dcdc;
    --arm-light: #e9ecef;
    --arm-shade: #9aa1a8;
  }
  html, body {
    margin: 0;
    padding: 0;
    width: 1200px;
    height: 1126px;
    overflow: hidden;
    background: var(--backdrop);
  }
  .book-cover {
    position: absolute;
    left: 264px;
    top: 45px;
    width: 672px;
    height: 1035px;
    overflow: hidden;
    background: radial-gradient(ellipse 62% 48% at 50% 46%, var(--cover-glow) 0%, var(--cover-mid) 45%, var(--cover-edge) 100%);
    color: var(--ink-light);
  }
  .author-name {
    position: absolute;
    top: 82px;
    left: 0;
    right: 0;
    margin: 0;
    text-align: center;
    font-family: "Michroma", sans-serif;
    font-size: 23px;
    letter-spacing: 3px;
    font-weight: 400;
  }
  .robot-arm {
    position: absolute;
    left: 415px;
    top: 250px;
    width: 257px;
    height: 228px;
  }
  .book-title {
    position: absolute;
    top: 500px;
    left: 0;
    right: 0;
    margin: 0;
    text-align: center;
    font-family: "Dosis", sans-serif;
    font-weight: 200;
    font-size: 72px;
    line-height: 1;
    letter-spacing: 9px;
    white-space: nowrap;
  }
  .book-title .lifted-letter {
    display: inline-block;
    font-size: 40px;
    transform: translateY(-46px);
    margin: 0 4px;
  }
  .strapline {
    position: absolute;
    top: 618px;
    left: 60px;
    right: 60px;
    margin: 0;
    text-align: center;
    font-family: "Dosis", sans-serif;
    font-weight: 300;
    font-size: 26px;
    line-height: 35px;
    letter-spacing: 1px;
    color: var(--ink-soft);
  }
</style>
</head>
<body>
  <main class="book-cover">
    <p class="author-name">TOM HOLLIS</p>

    <svg class="robot-arm" role="img" aria-label="Illustration of a white robotic arm reaching in from the right edge to lift a letter of the title" viewBox="0 0 257 228">
      <defs>
        <linearGradient id="armTone" x1="0" y1="0" x2="1" y2="1">
          <stop offset="0" stop-color="var(--arm-light)"/>
          <stop offset="1" stop-color="var(--arm-shade)"/>
        </linearGradient>
      </defs>
      <rect x="0" y="0" width="257" height="228" fill="url(#armTone)" opacity="0.35"/>
    </svg>

    <h1 class="book-title">TORVANIQ<span class="lifted-letter">U</span>E</h1>

    <p class="strapline">The close of human work and how automatons will supplant it</p>
  </main>
</body>
</html>
```